K7 Digital Stationery Design Project

We are looking to have stationary designs created for our company branding materials. We are looking for the following to be created.
1. Business Cards (front & back)
2. Letterhead
3. Envelopes #10
We are a new web design, development and marketing firm. Primary color scheme is desired to be blue/grey/white. This web start-up is owned and operated by individuals with 15+ years experience each in the industry so should not look as though it is a start-up by young/inexperienced individuals.
We build website & custom applications/software. In addition we provide the full spectrum of web marketing solutions including SEO, PPC, Social Media, Branding, Content Marketing and PR.
Please let us know if you have any questions. Looking forward to seeing all the amazing design ideas.
Attached is our logo.
Thanks!
Target Market(s)
Company will be nearly 100% business to business sales. Looking to work with companies that are already established, with a website, who want to take their website and/or online marketing efforts to the next level.
Industry/Entity Type
Marketing
Look and feel

```html
<!DOCTYPE html>
<html lang="en">
<head>
<meta charset="utf-8">
<title>K7 Digital Stationery</title>
<link rel="stylesheet" href="https://fonts.googleapis.com/css2?family=Jost:wght@400;500;700&display=swap">
<style>
  :root {
    --backdrop: #ebe7e1;
    --charcoal: #3c3c3e;
    --charcoal-light: #48484b;
    --paper: #ffffff;
    --paper-shade: #f1f1f1;
    --blue: #1b8fd8;
    --blue-deep: #1a6ec6;
    --ink: #333335;
    --ink-soft: #6a6a6d;
    --on-dark: #ffffff;
    --on-dark-soft: #b5b5b8;
  }
  * { box-sizing: border-box; margin: 0; padding: 0; }
  html, body { width: 1200px; height: 900px; overflow: hidden; }
  body {
    background: var(--backdrop);
    font-family: "Jost", "Futura", sans-serif;
    color: var(--ink);
    position: relative;
  }
  .sheet {
    position: absolute;
    box-shadow: 0 2px 6px rgba(0,0,0,.18);
  }
  .sheet--dark {
    background: radial-gradient(ellipse at center, var(--charcoal-light) 0%, var(--charcoal) 70%);
    color: var(--on-dark);
  }
  .sheet--light {
    background: radial-gradient(ellipse at center, var(--paper) 30%, var(--paper-shade) 100%);
  }

  /* brand name block */
  .brand { display: flex; align-items: center; gap: 8px; }
  .brand__dot { border-radius: 50%; background: linear-gradient(180deg, var(--blue), var(--blue-deep)); flex: none; }
  .brand__name { font-weight: 700; letter-spacing: .02em; line-height: 1; text-transform: uppercase; }
  .brand__tagline { font-weight: 500; line-height: 1.2; }

  /* letterhead */
  .letterhead { left: 60px; top: 38px; width: 450px; height: 580px; background: var(--paper); }
  .letterhead__head { position: absolute; left: 22px; top: 20px; display: flex; align-items: center; gap: 14px; }
  .letterhead .brand__dot { width: 16px; height: 16px; }
  .letterhead .brand__name { font-size: 15px; color: var(--ink); }
  .letterhead .brand__tagline { font-size: 7px; color: var(--ink); margin-top: 3px; }
  .letterhead__contact { border-left: 1px solid var(--ink-soft); padding-left: 6px; font-size: 6px; line-height: 1.45; color: var(--ink-soft); }

  /* folder */
  .folder { left: 30px; top: 135px; width: 450px; height: 580px; }
  .folder__mark { position: absolute; left: 0; right: 0; top: 250px; display: flex; flex-direction: column; align-items: center; gap: 14px; }
  .folder .brand__dot { width: 44px; height: 44px; }
  .folder .brand__name { font-size: 30px; color: var(--on-dark); }

  /* envelope back */
  .envelope-back { left: 615px; top: 34px; width: 555px; height: 230px; overflow: hidden; }
  .envelope-back__flap { position: absolute; left: 0; top: 0; width: 100%; height: 42px; }
  .envelope-back__brand { position: absolute; left: 0; right: 0; bottom: 24px; text-align: center; }
  .envelope-back .brand__name { font-size: 16px; color: var(--ink); }
  .envelope-back .brand__tagline { font-size: 7px; color: var(--ink); margin-top: 2px; }

  /* envelope front */
  .envelope-front { left: 615px; top: 290px; width: 555px; height: 240px; }
  .envelope-front__head { position: absolute; left: 14px; top: 16px; }
  .envelope-front .brand__dot { width: 18px; height: 18px; }
  .envelope-front .brand__name { font-size: 16px; color: var(--on-dark); }
  .envelope-front .brand__tagline { font-size: 7px; color: var(--on-dark); margin: 3px 0 0 26px; }
  .envelope-front__return { position: absolute; left: 14px; bottom: 14px; font-size: 6.5px; line-height: 1.4; color: var(--on-dark-soft); }
  .envelope-front__return span { margin-left: 18px; }

  /* business cards */
  .card-front-wide { left: 515px; top: 585px; width: 255px; height: 146px; }
  .card-front-wide .brand { position: absolute; left: 24px; top: 52px; }
  .card-front-wide .brand__dot { width: 20px; height: 20px; }
  .card-front-wide .brand__name { font-size: 20px; color: var(--on-dark); }
  .card-front-wide .brand__tagline { position: absolute; left: 52px; top: 78px; font-size: 8px; color: var(--on-dark); }

  .card-back-wide { left: 515px; top: 745px; width: 255px; height: 146px; }
  .card-back-wide__dot { position: absolute; left: 38px; top: 55px; }
  .card-back-wide .brand__dot { width: 26px; height: 26px; }
  .card-back-wide__details { position: absolute; left: 92px; top: 26px; border-left: 1px solid var(--ink-soft); padding-left: 8px; }
  .person__name { font-size: 10px; font-weight: 700; text-transform: uppercase; color: var(--ink); line-height: 1.2; }
  .person__role { font-size: 8px; font-weight: 700; text-transform: uppercase; color: var(--ink); margin-bottom: 10px; }
  .person__lines { font-size: 7px; line-height: 1.45; color: var(--ink-soft); }

  .card-front-tall { left: 800px; top: 560px; width: 146px; height: 255px; }
  .card-front-tall__mark { position: absolute; left: 0; right: 0; top: 96px; display: flex; flex-direction: column; align-items: center; gap: 8px; }
  .card-front-tall .brand__dot { width: 26px; height: 26px; }
  .card-front-tall .brand__name { font-size: 13px; color: var(--on-dark); }

  .card-back-tall { left: 975px; top: 560px; width: 146px; height: 255px; }
  .card-back-tall__brand { position: absolute; left: 0; right: 0; top: 38px; display: flex; flex-direction: column; align-items: center; gap: 6px; }
  .card-back-tall .brand__dot { width: 16px; height: 16px; }
  .card-back-tall .brand__name { font-size: 12px; color: var(--ink); }
  .card-back-tall .brand__tagline { font-size: 5.5px; color: var(--ink); }
  .card-back-tall__details { position: absolute; right: 14px; bottom: 22px; text-align: right; font-size: 6.5px; line-height: 1.45; color: var(--ink-soft); }
  .card-back-tall__details .person__name-small { font-size: 7px; color: var(--ink); }
</style>
</head>
<body>

  <!-- Letterhead -->
  <section class="sheet letterhead" aria-label="Letterhead">
    <header class="letterhead__head">
      <div>
        <div class="brand">
          <span class="brand__dot"></span>
          <span class="brand__name">K7 Digital</span>
        </div>
        <p class="brand__tagline">Web Design, Development and Marketing</p>
      </div>
      <address class="letterhead__contact" style="font-style:normal">
        (P) 0198-765-4321<br>
        (A) Your Business Address, State, Zip Code<br>
        (W) www.k7digital.com
      </address>
    </header>
  </section>

  <!-- Presentation folder -->
  <section class="sheet sheet--dark folder" aria-label="Presentation folder">
    <div class="folder__mark brand">
      <span class="brand__dot"></span>
      <span class="brand__name">K7 Digital</span>
    </div>
  </section>

  <!-- Envelope back -->
  <section class="sheet sheet--light envelope-back" aria-label="Envelope back">
    <svg class="envelope-back__flap" viewBox="0 0 555 42" preserveAspectRatio="none" aria-hidden="true">
      <polygon points="0,0 555,0 545,42 10,42" fill="var(--charcoal)"/>
    </svg>
    <div class="envelope-back__brand">
      <p class="brand__name">K7 Digital</p>
      <p class="brand__tagline">Web Design, Development and Marketing</p>
    </div>
  </section>

  <!-- Envelope front -->
  <section class="sheet sheet--dark envelope-front" aria-label="Envelope front">
    <div class="envelope-front__head">
      <div class="brand">
        <span class="brand__dot"></span>
        <span class="brand__name">K7 Digital</span>
      </div>
      <p class="brand__tagline">Web Design, Development and Marketing</p>
    </div>
    <p class="envelope-front__return">
      Your Business Address, City, State, Zip Code<br>
      0198-765-4321<span>www.k7digital.com</span>
    </p>
  </section>

  <!-- Business card front, landscape -->
  <section class="sheet sheet--dark card-front-wide" aria-label="Business card front">
    <div class="brand">
      <span class="brand__dot"></span>
      <span class="brand__name">K7 Digital</span>
    </div>
    <p class="brand__tagline">Web Design, Development and Marketing</p>
  </section>

  <!-- Business card back, landscape -->
  <section class="sheet sheet--light card-back-wide" aria-label="Business card back">
    <div class="card-back-wide__dot"><span class="brand__dot" style="display:block"></span></div>
    <div class="card-back-wide__details">
      <p class="person__name">Mr. Dorian Vale</p>
      <p class="person__role">Head Designer</p>
      <p class="person__lines">
        0198-765-4321<br>
        Your Business Address, State, Zip Code<br>
        hello@k7digital.com<br>
        www.k7digital.com
      </p>
    </div>
  </section>

  <!-- Business card front, portrait -->
  <section class="sheet sheet--dark card-front-tall" aria-label="Business card front, portrait">
    <div class="card-front-tall__mark brand">
      <span class="brand__dot"></span>
      <span class="brand__name">K7 Digital</span>
    </div>
  </section>

  <!-- Business card back, portrait -->
  <section class="sheet sheet--light card-back-tall" aria-label="Business card back, portrait">
    <div class="card-back-tall__brand">
      <span class="brand__dot"></span>
      <span class="brand__name">K7 Digital</span>
      <span class="brand__tagline">Web Design, Development and Marketing</span>
    </div>
    <div class="card-back-tall__details">
      <p class="person__name-small">Mr. Dorian Vale</p>
      <p>Head Designer</p>
      <p style="margin-top:6px">Your Business Address,<br>City, State, Zip Code</p>
      <p style="margin-top:6px">(P) 0198-765-4321<br>hello@k7digital.com</p>
    </div>
  </section>

</body>
</html>
```